Brivet Networks, Inc. Website redesign

Revamp the website, it is old and outdated. www.brivetnetworksinc.com

Target Market(s)

Information Technology Consulting and Staffing

Coding

Coded - Design and coding required

Number of Pages Required

5+ page

Colors

Designer to choose colors to be used in the design.

Requirements
Must have
• Outlined text boxes just like from the Hollis.us site. A clean look

```html
<!DOCTYPE html>
<html lang="en">
<head>
<meta charset="utf-8">
<title>Brivet Networks, Inc.</title>
<link href="https://fonts.googleapis.com/css2?family=Lato:wght@400;700&family=Orbitron:wght@700;800&display=swap" rel="stylesheet">
<style>
:root{
  --red:#9e1b32;
  --red-bright:#a51d35;
  --ink:#1a1a1a;
  --text:#555;
  --muted:#6d6d6d;
  --light:#f5f5f5;
  --line:#e6e6e6;
  --dark:#222427;
  --white:#fff;
}
*{margin:0;padding:0;box-sizing:border-box}
html,body{width:1200px;height:3792px;overflow:hidden}
body{font-family:"Lato",sans-serif;color:var(--text);background:var(--white);position:relative}
.abs{position:absolute}
h2,.display{font-family:"Orbitron",sans-serif;font-weight:800;color:var(--ink);letter-spacing:.5px}

/* hero */
.hero{position:absolute;left:0;top:0;width:1200px;height:645px;background:linear-gradient(100deg,#2b3038 0%,#1f242b 45%,#161a20 100%);overflow:hidden}
.hero-photo{position:absolute;left:0;top:0;width:1200px;height:645px;background:radial-gradient(ellipse at 25% 45%,#4a4f57 0%,#2a2e35 40%,rgba(20,23,28,0) 75%)}
.hero-band{position:absolute;left:0;top:0}
.site-header{position:absolute;left:0;top:0;width:1200px;height:94px;border-bottom:1px solid rgba(255,255,255,.22)}
.brand{position:absolute;left:77px;top:32px;font-family:"Lato",sans-serif;font-weight:700;font-size:22px;color:var(--white);letter-spacing:2px}
.nav{position:absolute;top:38px;left:0;font-size:13px;color:var(--white);letter-spacing:.3px}
.nav a{position:absolute;white-space:nowrap;color:var(--white);text-decoration:none}
.nav .active::after{content:"";position:absolute;left:-4px;right:-4px;top:52px;height:2px;background:var(--red)}
.phone{position:absolute;left:986px;top:37px;color:var(--white);font-size:16px;display:flex;align-items:center;gap:10px}
.hero-words{position:absolute;font-family:"Orbitron",sans-serif;font-weight:800;font-size:40px;color:var(--white);letter-spacing:1px;line-height:1}

/* welcome */
.section-title{position:absolute;left:0;width:1200px;text-align:center;font-size:33px}
.welcome-sub{position:absolute;left:0;top:751px;width:1200px;text-align:center;color:var(--red);font-size:19px}
.card{position:absolute;background:var(--white);box-shadow:0 2px 14px rgba(0,0,0,.09)}
.photo{position:absolute;overflow:hidden}
.photo .slash{position:absolute;right:0;bottom:0}
.copy{font-size:13.5px;line-height:25px;color:var(--text)}
.copy p+p{margin-top:13px}
.read-more{position:absolute;left:78px;top:1605px;color:var(--red);font-weight:700;font-size:16px;text-decoration:underline;display:flex;align-items:center;gap:10px}

/* services */
.services{position:absolute;left:77px;top:1845px;width:1045px;height:415px;background:var(--white);box-shadow:0 2px 14px rgba(0,0,0,.08);display:flex}
.service{flex:1;position:relative;text-align:center;padding-top:62px;border-left:1px solid var(--line);margin:18px 0}
.service:first-child{border-left:none}
.service svg.icon{display:block;margin:0 auto}
.service h3{font-weight:400;font-size:19px;color:var(--ink);margin-top:22px}
.service p{font-size:14px;line-height:25px;color:var(--muted);margin:14px auto 0;width:230px}
.diamond{position:absolute;left:50%;top:286px;width:48px;height:48px;margin-left:-24px;background:var(--red);transform:rotate(45deg);display:flex;align-items:center;justify-content:center}
.diamond svg{transform:rotate(-45deg)}

/* strategy */
.strategy{position:absolute;left:0;top:2354px;width:1200px;height:500px;background:radial-gradient(ellipse at 75% 30%,#3a3c40 0%,#26282b 45%,#1b1c1f 100%)}
.strategy h2{position:absolute;left:0;top:64px;width:1200px;text-align:center;color:var(--white);font-size:33px}
.strategy .tag{position:absolute;left:0;top:126px;width:1200px;text-align:center;color:var(--white);font-size:19px}
.strategy .copy{position:absolute;left:150px;top:177px;width:900px;text-align:center;color:#e8e8e8;font-size:14px}
.btn{position:absolute;top:360px;height:50px;width:197px;background:var(--red);color:var(--white);font-family:"Orbitron",sans-serif;font-weight:700;font-size:16px;display:flex;align-items:center;justify-content:center;letter-spacing:.5px}

/* news */
.news{position:absolute;left:0;top:2853px;width:1200px;height:669px;background:var(--light)}
.news-card{position:absolute;top:120px;width:322px;height:468px;background:var(--white)}
.news-img{width:322px;height:228px}
.news-body{padding:0 17px}
.news-date{color:var(--red);font-size:14px;margin-top:33px}
.news-title{color:var(--ink);font-size:16px;line-height:27px;margin-top:12px}
.news-text{color:var(--muted);font-size:13.5px;line-height:27px;margin-top:12px}

/* footer */
.footer{position:absolute;left:0;top:3522px;width:1200px;height:270px;background:var(--red)}
.social{position:absolute;top:51px;width:56px;height:56px;border:2px solid var(--white);border-radius:50%}
.foot-nav{position:absolute;left:0;top:140px;width:1200px;text-align:center;color:var(--white);font-size:14px}
.foot-nav span{margin:0 18px}
.copyright{position:absolute;left:0;top:232px;width:1200px;text-align:center;color:var(--white);font-size:13px}
</style>
</head>
<body>

<section class="hero">
  <div class="hero-photo" role="img" aria-label="Businessman in a shirt and tie with arms crossed in a dark server room"></div>
  <svg class="hero-band" width="1200" height="645" viewBox="0 0 1200 645" aria-hidden="true">
    <polygon points="1004,0 1148,0 905,645 739,645" fill="#a51d35"/>
  </svg>
  <header class="site-header">
    <div class="brand">BRIVET NETWORKS</div>
    <nav class="nav">
      <a class="active" style="left:446px">HOME</a>
      <a style="left:517px">ABOUT US</a>
      <a style="left:613px">SERVICES</a>
      <a style="left:702px">STRATEGY</a>
      <a style="left:797px">IT NEWS</a>
      <a style="left:879px">CONTACT</a>
    </nav>
    <div class="phone">
      <svg width="18" height="18" viewBox="0 0 24 24" aria-hidden="true"><path fill="#fff" d="M6.6 10.8c1.4 2.8 3.8 5.1 6.6 6.6l2.2-2.2c.3-.3.7-.4 1-.2 1.1.4 2.3.6 3.6.6.6 0 1 .4 1 1V20c0 .6-.4 1-1 1C10.6 21 3 13.4 3 4c0-.6.4-1 1-1h3.5c.6 0 1 .4 1 1 0 1.3.2 2.5.6 3.6.1.3 0 .7-.2 1L6.6 10.8z"/></svg>
      301-555-0148
    </div>
  </header>
  <div class="hero-words" style="left:784px;top:263px">INTEGRITY</div>
  <div class="hero-words" style="left:790px;top:333px">MISSION</div>
  <div class="hero-words" style="left:753px;top:404px">RESULTS</div>
</section>

<h2 class="section-title" style="top:696px">WELCOME VISITORS!</h2>
<div class="welcome-sub">Bringing Thought Leadership and Quality to Every Project</div>

<article class="card" style="left:77px;top:833px;width:1045px;height:438px">
  <div class="photo" style="left:0;top:0;width:416px;height:438px;background:linear-gradient(135deg,#1c3d6b 0%,#2f6aa8 45%,#0f2444 100%)" role="img" aria-label="Two IT engineers reviewing a tablet in a lit data center aisle">
    <svg class="slash" width="416" height="438" viewBox="0 0 416 438" aria-hidden="true"><polygon points="416,228 416,438 276,438" fill="#a51d35"/></svg>
  </div>
  <div class="copy abs" style="left:487px;top:71px;width:510px">
    <p>Brivet Networks, Inc. is an 8(a) full-service IT consulting company based in the Washington, DC Metro area. We offer specialized, highly customized technology solutions for our customers located throughout the United States. Learn about our Services now.</p>
    <p>No two businesses are the same. We believe the technology supporting your business operations should align with your company. Every project begins with a thorough analysis of your current technology environment. We work with you to define the environment you want. Then we implement industry-proven practices that enable you to achieve your business objectives. We draw on our experience at civilian and federal agencies to generate ideas and create IT solutions that address your unique business needs. Learn about our Strategies.</p>
  </div>
</article>

<h2 class="abs" style="left:78px;top:1343px;font-size:34px">ABOUT US</h2>
<div class="copy abs" style="left:78px;top:1395px;width:510px">
  <p>Brivet Networks, Inc. is an 8(a) innovative and rapidly growing full-service IT consulting firm. We provide our clients with cutting-edge technologies and the know-how to apply them to their individual business models.</p>
  <p>For over 20 + years, we have been providing reliable IT solutions to businesses in the Washington, DC Metro area and beyond. Our comprehensive services provide clients with unique technology solutions that are customized to meet the specific demands of their business.</p>
</div>
<a class="read-more">READ MORE <svg width="34" height="14" viewBox="0 0 34 14" aria-hidden="true"><path d="M0 7h31M25 1l7 6-7 6" stroke="#9e1b32" stroke-width="2" fill="none"/></svg></a>
<div class="photo" style="left:707px;top:1271px;width:415px;height:437px;background:linear-gradient(160deg,#cfd3d6 0%,#a79a8c 45%,#6f5a44 100%)" role="img" aria-label="Smiling team working on laptops around an office table">
  <svg class="slash" width="415" height="437" viewBox="0 0 415 437" aria-hidden="true"><polygon points="415,222 415,437 276,437" fill="#a51d35"/></svg>
</div>

<h2 class="section-title" style="top:1770px">OUR SERVICES</h2>
<div class="services">
  <div class="service">
    <svg class="icon" width="62" height="62" viewBox="0 0 62 62" fill="none" stroke="#9e1b32" stroke-width="2" aria-hidden="true"><rect x="3" y="6" width="56" height="38" rx="2"/><path d="M3 38h56M24 44l-3 10M38 44l3 10M16 56h30"/><circle cx="31" cy="22" r="11"/><path d="M26 22h10M31 17v10M27 18l8 8M35 18l-8 8"/></svg>
    <h3>Hardware / Software Sales</h3>
    <p>We have access to multiple distributor partners throughout North America, as well...</p>
    <div class="diamond"><svg width="20" height="14" viewBox="0 0 20 14"><path d="M0 7h18M12 1l6 6-6 6" stroke="#fff" stroke-width="1.8" fill="none"/></svg></div>
  </div>
  <div class="service">
    <svg class="icon" width="62" height="62" viewBox="0 0 62 62" fill="none" stroke="#9e1b32" stroke-width="2" aria-hidden="true"><path d="M27 3h8l1 6 5 2 5-4 6 6-4 5 2 5 6 1v8l-6 1-2 5 4 5-6 6-5-4-5 2-1 6h-8l-1-6-5-2-5 4-6-6 4-5-2-5-6-1v-8l6-1 2-5-4-5 6-6 5 4 5-2z"/><circle cx="31" cy="31" r="15"/><circle cx="31" cy="27" r="5"/><path d="M22 41c2-6 16-6 18 0"/></svg>
    <h3>Professional Services</h3>
    <p>Our team provides experienced leadership and guidance, utilizing the industry standard...</p>
    <div class="diamond"><svg width="20" height="14" viewBox="0 0 20 14"><path d="M0 7h18M12 1l6 6-6 6" stroke="#fff" stroke-width="1.8" fill="none"/></svg></div>
  </div>
  <div class="service">
    <svg class="icon" width="62" height="62" viewBox="0 0 62 62" fill="none" stroke="#9e1b32" stroke-width="2" aria-hidden="true"><rect x="20" y="18" width="22" height="26"/><circle cx="31" cy="28" r="5"/><path d="M28 34h6v4h-6zM26 18V4M36 18V4M26 44v14M36 44v14M20 26H6M20 36H6M42 26h14M42 36h14"/><rect x="22" y="1" width="8" height="5"/><rect x="4" y="23" width="5" height="6"/><rect x="53" y="33" width="5" height="6"/><rect x="32" y="56" width="8" height="5"/></svg>
    <h3>Technology Assessment</h3>
    <p>Experience has shown companies that perform objective, third-party technology assessments have...</p>
    <div class="diamond"><svg width="20" height="14" viewBox="0 0 20 14"><path d="M0 7h18M12 1l6 6-6 6" stroke="#fff" stroke-width="1.8" fill="none"/></svg></div>
  </div>
  <div class="service">
    <svg class="icon" width="62" height="62" viewBox="0 0 62 62" fill="none" stroke="#9e1b32" stroke-width="2" aria-hidden="true"><rect x="8" y="14" width="46" height="34" rx="2"/><path d="M2 48h58v5H2z"/><rect x="18" y="4" width="26" height="30"/><path d="M23 11h16M23 16h16M23 21h10"/><circle cx="31" cy="40" r="4"/><path d="M24 48c1-4 13-4 14 0"/></svg>
    <h3>Technology Consulting</h3>
    <p>Implementing quality solutions is more than applying technology to problems. You need experts...</p>
    <div class="diamond"><svg width="20" height="14" viewBox="0 0 20 14"><path d="M0 7h18M12 1l6 6-6 6" stroke="#fff" stroke-width="1.8" fill="none"/></svg></div>
  </div>
</div>

<section class="strategy" role="img" aria-label="Dark background of hands typing on a keyboard">
  <h2>OUR STRATEGY</h2>
  <div class="tag">Your Path to Success</div>
  <div class="copy">
    <p>Civilian and Federal agencies are facing increased demands driven by the changing economic environment and shifts in the way products and services are sold and delivered. These factors have created an imperative to leverage new and innovative technology solution architectures like cloud computing to help reduce cost and deliver profit-driving IT capabilities faster than ever before.</p>
    <p>Savvy businesses understand that technology investments cannot be made solely to enable internal and external operations; technology is now, more than ever, a critical component to retaining and winning customers as well as staying ahead of the competition.</p>
  </div>
  <div class="btn" style="left:392px">LEARN MORE</div>
  <div class="btn" style="left:611px">CONTACT US</div>
</section>

<section class="news">
  <h2 class="section-title" style="top:53px">IT NEWS</h2>
  <article class="news-card" style="left:77px">
    <div class="news-img" style="background:linear-gradient(135deg,#e9e5df 0%,#b9aa98 50%,#6b6258 100%)" role="img" aria-label="Hands typing on a laptop keyboard"></div>
    <div class="news-body">
      <div class="news-date">05 SEP 2019</div>
      <div class="news-title">Lorem ipsum dolor sit amet, consectet adipiscing elit, sed do eiusmod tempor</div>
      <div class="news-text">Lorem ipsum dolor sit amet, consectetur adi elit, sed do eiusmod tempor incididunt ut lab et dolore magna aliqua. Ut enim ad minim.</div>
    </div>
  </article>
  <article class="news-card" style="left:439px">
    <div class="news-img" style="background:linear-gradient(135deg,#3c3028 0%,#6b574a 50%,#2a2420 100%)" role="img" aria-label="Team gathered around a laptop working late"></div>
    <div class="news-body">
      <div class="news-date">05 SEP 2019</div>
      <div class="news-title">Lorem ipsum dolor sit amet, consectet adipiscing elit, sed do eiusmod tempor</div>
      <div class="news-text">Lorem ipsum dolor sit amet, consectetur adi elit, sed do eiusmod tempor incididunt ut lab et dolore magna aliqua. Ut enim ad minim.</div>
    </div>
  </article>
  <article class="news-card" style="left:800px">
    <div class="news-img" style="background:linear-gradient(135deg,#2a3a4f 0%,#5a6f86 50%,#1d2633 100%)" role="img" aria-label="Two engineers with a laptop inspecting server racks"></div>
    <div class="news-body">
      <div class="news-date">05 SEP 2019</div>
      <div class="news-title">Lorem ipsum dolor sit amet, consectet adipiscing elit, sed do eiusmod tempor</div>
      <div class="news-text">Lorem ipsum dolor sit amet, consectetur adi elit, sed do eiusmod tempor incididunt ut lab et dolore magna aliqua. Ut enim ad minim.</div>
    </div>
  </article>
</section>

<footer class="footer">
  <div class="social" style="left:536px" aria-label="Social profile"></div>
  <div class="social" style="left:607px" aria-label="Social profile"></div>
  <div class="foot-nav">Home<span>|</span>About us<span>|</span>Services<span>|</span>Strategy<span>|</span>IT News<span>|</span>Contact</div>
  <div class="copyright">©BRIVET NETWORKS. 2019 - All Rights Reserved.</div>
</footer>

</body>
</html>
```